Football and Sports Management Agency Stationary

We have a logo, fonts, website and colour palette.
We need the logo refined by a proper designer and then business stationary designed. You can see on the website how it needs adjusting by a designers eye.
The company is a high end sports management company aiming to attract and represent professional athletes. The name Veltor is to indicate a 'Constellation of Stars' ie our clients. The dots on the star should be slightly different sizes to reflect that some clients will be bigger than others.
Colours:
#e6e6e6
#edd2a4
#caaa72 (main gold and also used on site)
#3f3f42
#001d38
#edeced (on website)
#191c23 (on website)
Font:
LS (veltor)
SF Florencesans (sports management)
We would like:
- Letterhead (word and indesign and PDF print format). I have attached an example for one I like. It's quiet a clean design with the contact details and address taking up only a small amount of room.
- Business card (dark on the back with the logo, personal details on the front). Only needs name, title, email, website and phone number. No company address (in PDF and indesign format)
- Powerpoint slide theme
- Logo in vector format for light and dark versions and single colour versions. And optimised web version
- Simple brand guide PDF showing colour, font and logo (a one/two page PDF)
Any questions, please ask.
NEW INFO:
Contact Details
Maren Odsworth
Director
Mobile: +44 7312 908 271
Phone: +44 0113 872 604
Email: maren@veltorathletic-example.com
Web: veltorathletic-example.com
Bramwell Court, 14 Orchard Rise, Larchmere, Ashvale, LV9 2QT
Company number 20948367
Target Market(s)
Professional athletes, professional sports teams.
Industry/Entity Type
Management
Requirements
Must have
- NEW
- The designs must look cool, classy and high quality. My suggestion for this is to keep the text small and precise with uncomplicated design.
Nice to have
- Application of brand displayed on stationary and additional pieces of stationary branded.
- Draw some inspiration from the website. eg the slant angles used separate the sections.
Should not have
- Don't create new logos etc.

```html
<!DOCTYPE html>
<html lang="en">
<head>
<meta charset="utf-8">
<title>Veltor Stationery Set</title>
<link href="https://fonts.googleapis.com/css2?family=Jost:wght@300;400;500&display=swap" rel="stylesheet">
<style>
:root{
  --gold:#caaa72;
  --gold-light:#edd2a4;
  --paper:#edeced;
  --paper-white:#f4f4f3;
  --slide:#e6e6e6;
  --charcoal:#3f3f42;
  --ink:#191c23;
  --night:#2a2c31;
  --stage:#161616;
  --text:#2b2b2e;
}
*{margin:0;padding:0;box-sizing:border-box}
html,body{width:1028px;height:1200px;overflow:hidden;background:var(--stage)}
body{position:relative;font-family:"Jost",sans-serif;color:var(--text)}
.piece{position:absolute;overflow:hidden}
.wordmark{font-family:"Jost",sans-serif;font-weight:300;letter-spacing:.42em;display:flex;align-items:center;gap:.35em;white-space:nowrap}
.wordmark .dot{display:inline-block;border-radius:50%;background:var(--gold)}
.tiny{font-size:4px;line-height:1.45}

/* letterhead */
.letterhead{left:217px;top:94px;width:279px;height:395px;background:var(--paper-white)}
.letterhead .wordmark{position:absolute;left:26px;top:48px;font-size:9px;color:var(--charcoal)}
.letterhead .wordmark .dot{width:4px;height:4px}
.letterhead .contact{position:absolute;right:24px;top:28px;width:70px;color:#555}
.letterhead .contact .ic{color:var(--gold)}
.letterhead .footer{position:absolute;left:0;bottom:0;width:100%;height:16px}
.letterhead .footer-url{position:absolute;left:22px;bottom:4px;font-size:4px;letter-spacing:.12em;color:#fff}

/* folder */
.folder{left:545px;top:76px;width:330px;height:418px;background:var(--night)}
.folder .wordmark{position:absolute;left:0;right:0;top:200px;justify-content:center;font-size:22px;color:#f0f0f0}
.folder .wordmark .dot{width:7px;height:7px}

/* business cards */
.card-front{left:116px;top:526px;width:126px;height:70px;background:var(--paper-white)}
.card-front .wordmark{position:absolute;left:12px;top:36px;font-size:6px;color:var(--charcoal)}
.card-front .wordmark .dot{width:3px;height:3px}
.card-front .person{position:absolute;left:72px;top:21px}
.card-front .name{font-size:4.6px;font-weight:500;color:var(--ink);letter-spacing:.04em}
.card-front .role{font-size:3.4px;color:var(--gold);margin-bottom:2px}
.card-front .details{font-size:3px;line-height:1.5;color:#555}
.card-front .footer{position:absolute;left:0;bottom:0;width:100%;height:7px}
.card-back{left:116px;top:617px;width:126px;height:71px;background:var(--gold)}
.card-back .wordmark{position:absolute;left:0;right:0;top:27px;justify-content:center;font-size:7px;color:#fff}
.card-back .wordmark .dot{width:3px;height:3px;background:#fff}
.card-back .url{position:absolute;left:0;right:0;bottom:10px;text-align:center;font-size:3.4px;letter-spacing:.3em;color:#fff}

/* envelopes */
.envelope-front{left:275px;top:536px;width:314px;height:150px;background:var(--paper-white)}
.envelope-front .wordmark{position:absolute;left:22px;top:38px;font-size:9px;color:var(--charcoal)}
.envelope-front .wordmark .dot{width:4px;height:4px}
.envelope-front .address{position:absolute;left:22px;top:56px;font-size:4px;line-height:1.4;color:#555}
.envelope-back{left:619px;top:535px;width:313px;height:150px;background:var(--paper-white)}

/* slides */
.slide{width:257px;height:192px;background:var(--slide)}
.row1{top:733px}.row2{top:938px}
.col1{left:102px}.col2{left:383px}.col3{left:670px}
.slide .heading{position:absolute;left:14px;top:11px;font-size:10px;color:var(--gold);font-weight:400}
.slide .subheading{position:absolute;left:14px;top:25px;font-size:5.5px;font-weight:500;color:var(--ink)}
.slide .rule{position:absolute;left:56px;right:14px;top:30px;height:1px;background:#b5b5b5}
.slide .lorem{font-size:3.6px;line-height:1.5;color:#444}

.title-slide .wordmark{position:absolute;left:0;right:0;top:56px;justify-content:center;font-size:18px;color:var(--charcoal)}
.title-slide .wordmark .dot{width:6px;height:6px}
.title-slide .welcome{position:absolute;left:0;right:0;top:125px;text-align:center;font-size:11px;line-height:1.3;color:var(--ink)}
.title-slide .welcome .accent{color:var(--gold);font-size:12.5px;letter-spacing:.02em}

.team .photos{position:absolute;left:19px;top:54px;display:flex;gap:7px}
.team .photo{width:51px;height:51px;background:var(--charcoal);border:2px solid #fff;display:flex;align-items:center;justify-content:center;font-size:5.5px;color:#ddd}
.team .members{position:absolute;left:20px;top:118px;display:flex;gap:8px}
.team .member{width:50px}
.team .member-name{font-size:4.6px;color:var(--gold)}
.team .member-title{font-size:4.4px;font-style:italic;color:#444;margin-bottom:6px}

.groups .grid{position:absolute;left:15px;top:46px;right:14px;display:grid;grid-template-columns:1fr 1fr;column-gap:8px;row-gap:6px}
.groups .group-name{font-size:5.5px;color:var(--gold);margin-bottom:3px}

.chart-slide .bars{position:absolute;left:28px;top:50px}
.chart-slide .side-text{position:absolute;left:155px;top:46px;width:86px}
.chart-slide .bottom-text{position:absolute;left:20px;top:144px;right:20px}
.pie-slide .left-text{position:absolute;left:20px;top:62px;width:130px;text-align:center}
.pie-slide .left-text2{position:absolute;left:20px;top:134px;width:130px;text-align:center}
.pie-slide .pie{position:absolute;left:157px;top:54px}
.pie-slide .legend{position:absolute;left:158px;top:124px;font-size:3.4px;color:#444;line-height:2.6}
.pie-slide .legend i{display:inline-block;width:5px;height:5px;vertical-align:middle;margin-right:4px}
.pie-slide .legend-note{position:absolute;left:158px;top:150px;width:80px}

.thanks-slide{background:linear-gradient(160deg,#23262e,var(--ink))}
.thanks-slide .thanks{position:absolute;left:0;right:0;top:64px;text-align:center;font-size:34px;font-weight:300;color:var(--gold);line-height:1}
.thanks-slide .for-coming{position:absolute;left:0;right:0;top:98px;text-align:center;font-size:18px;font-weight:300;color:#f0f0f0}
.thanks-slide .footer-info{position:absolute;left:0;right:0;bottom:12px;text-align:center;font-size:4px;line-height:1.45;color:#ddd}
.thanks-slide .footer-info .gold{color:var(--gold)}

.fill-gold{fill:var(--gold)}
.fill-ink{fill:var(--ink)}
.fill-night{fill:var(--night)}
</style>
</head>
<body>

<!-- Letterhead -->
<section class="piece letterhead">
  <div class="wordmark"><span class="dot"></span>VELTOR</div>
  <div class="contact tiny">
    Bramwell Court, 14 Orchard Rise<br>Larchmere, Ashvale, LV9 2QT<br>Company number 20948367<br>
    <span class="ic">&#9742;</span> +44 0113 872 604<br>
    <span class="ic">&#9647;</span> +44 7312 908 271<br>
    <span class="ic">&#9993;</span> maren@veltorathletic-example.com
  </div>
  <svg class="footer" viewBox="0 0 279 16" preserveAspectRatio="none">
    <rect class="fill-ink" x="0" y="9" width="279" height="7"/>
    <path class="fill-gold" d="M0 3 H100 Q106 3 108 9 L110 16 H0 Z"/>
  </svg>
  <div class="footer-url">www.veltorathletic-example.com</div>
</section>

<!-- Presentation folder -->
<section class="piece folder">
  <div class="wordmark"><span class="dot"></span>VELTOR</div>
</section>

<!-- Business card front -->
<section class="piece card-front">
  <div class="wordmark"><span class="dot"></span>VELTOR</div>
  <div class="person">
    <div class="name">MAREN ODSWORTH</div>
    <div class="role">DIRECTOR</div>
    <div class="details">+44 7312 908 271<br>+44 0113 872 604<br>maren@veltorathletic-example.com</div>
  </div>
  <svg class="footer" viewBox="0 0 126 7" preserveAspectRatio="none">
    <rect class="fill-ink" x="0" y="3" width="126" height="4"/>
    <path class="fill-gold" d="M0 0 H64 Q67 0 68 3 L69 7 H0 Z"/>
  </svg>
</section>

<!-- Business card back -->
<section class="piece card-back">
  <div class="wordmark"><span class="dot"></span>VELTOR</div>
  <div class="url">www.veltorathletic-example.com</div>
</section>

<!-- Envelope front -->
<section class="piece envelope-front">
  <div class="wordmark"><span class="dot"></span>VELTOR</div>
  <div class="address">Bramwell Court, 14 Orchard Rise<br>Larchmere, Ashvale, LV9 2QT</div>
</section>

<!-- Envelope back -->
<section class="piece envelope-back">
  <svg width="313" height="150" viewBox="0 0 313 150">
    <path class="fill-night" d="M0 0 H313 V16 L302 50 H11 L0 16 Z"/>
  </svg>
</section>

<!-- Slide: title -->
<section class="piece slide title-slide row1 col1">
  <div class="wordmark"><span class="dot"></span>VELTOR</div>
  <div class="welcome">WELCOME TO OUR<br><span class="accent">PRESENTATION NAME</span><br>DESCRIPTION</div>
</section>

<!-- Slide: team -->
<section class="piece slide team row1 col2">
  <div class="heading">Heading Here</div>
  <div class="subheading">Sub Heading</div>
  <div class="rule"></div>
  <div class="photos">
    <div class="photo">Photo</div><div class="photo">Photo</div><div class="photo">Photo</div><div class="photo">Photo</div>
  </div>
  <div class="members">
    <div class="member"><div class="member-name">Team member1</div><div class="member-title">Title</div><div class="lorem">Lorem ipsum dolor sit amet, consectetur adipisicing elit, sed do eiusmod tempor incididunt</div></div>
    <div class="member"><div class="member-name">Team member2</div><div class="member-title">Title</div><div class="lorem">ut labore et dolore magna aliqua. Ut enim ad minim veniam, quis nostrud exercitation</div></div>
    <div class="member"><div class="member-name">Team member3</div><div class="member-title">Title</div><div class="lorem">ullamco laboris nisi ut aliquip ex ea commodo consequat enim ad minim veniam.</div></div>
    <div class="member"><div class="member-name">Team member4</div><div class="member-title">Title</div><div class="lorem">Do eiusmod tempor incididunt. Lorem ipsum dolor sit amet, consectetur adipisicing elit, sed</div></div>
  </div>
</section>

<!-- Slide: groups -->
<section class="piece slide groups row1 col3">
  <div class="heading">Heading Here</div>
  <div class="subheading">Sub Heading</div>
  <div class="rule"></div>
  <div class="grid">
    <div><div class="group-name">Group1</div><div class="lorem">Lorem ipsum dolor sit amet, consectetur adipisicing elit, sed do eiusmod tempor incididunt ut labore et dolore magna aliqua. Ut enim ad minim veniam, quis nostrud exercitation ullamco laboris nisi ut aliquip ex ea commodo consequat.</div></div>
    <div><div class="group-name">Group4</div><div class="lorem">Lorem ipsum dolor sit amet, consectetur adipisicing elit, sed do eiusmod tempor incididunt ut labore et dolore magna aliqua. Ut enim ad minim veniam, quis nostrud exercitation ullamco laboris nisi ut aliquip ex ea commodo consequat.</div></div>
    <div><div class="group-name">Group2</div><div class="lorem">Duis aute irure dolor in reprehenderit in voluptate velit esse cillum dolore eu fugiat nulla pariatur. Excepteur sint occaecat cupidatat non proident, sunt in culpa qui officia deserunt mollit anim id est laborum.</div></div>
    <div><div class="group-name">Group5</div><div class="lorem">Duis aute irure dolor in reprehenderit in voluptate velit esse cillum dolore eu fugiat nulla pariatur. Excepteur sint occaecat cupidatat non proident, sunt in culpa qui officia deserunt mollit anim id est laborum.</div></div>
    <div><div class="group-name">Group3</div><div class="lorem">Duis aute irure dolor in reprehenderit in voluptate velit esse cillum dolore eu fugiat nulla pariatur. Excepteur sint occaecat cupidatat non proident, sunt in culpa qui officia deserunt mollit anim id est laborum.</div></div>
    <div><div class="group-name">Group6</div><div class="lorem">Duis aute irure dolor in reprehenderit in voluptate velit esse cillum dolore eu fugiat nulla pariatur. Excepteur sint occaecat cupidatat non proident, sunt in culpa qui officia deserunt mollit anim id est laborum.</div></div>
  </div>
</section>

<!-- Slide: bar chart -->
<section class="piece slide chart-slide row2 col1">
  <div class="heading">Heading Here</div>
  <div class="subheading">Sub Heading</div>
  <div class="rule"></div>
  <svg class="bars" width="104" height="78" viewBox="0 0 104 78">
    <g stroke="#c9c9c9" stroke-width=".6">
      <line x1="0" y1="2" x2="104" y2="2"/><line x1="0" y1="10" x2="104" y2="10"/><line x1="0" y1="18" x2="104" y2="18"/>
      <line x1="0" y1="26" x2="104" y2="26"/><line x1="0" y1="34" x2="104" y2="34"/><line x1="0" y1="42" x2="104" y2="42"/>
      <line x1="0" y1="50" x2="104" y2="50"/><line x1="0" y1="58" x2="104" y2="58"/><line x1="0" y1="66" x2="104" y2="66"/>
      <line x1="0" y1="74" x2="104" y2="74"/>
    </g>
    <g class="fill-gold">
      <rect x="33" y="2" width="13" height="74"/><rect x="48" y="12" width="13" height="64"/>
      <rect x="63" y="34" width="13" height="42"/><rect x="78" y="19" width="13" height="57"/>
    </g>
    <g fill="#fff" font-size="3.6" font-family="Jost, sans-serif">
      <text transform="translate(41 72) rotate(-90)">Sub head1</text>
      <text transform="translate(56 72) rotate(-90)">Sub head2</text>
      <text transform="translate(71 72) rotate(-90)">Sub head3</text>
      <text transform="translate(86 72) rotate(-90)">Sub head4</text>
    </g>
  </svg>
  <div class="side-text lorem">Lorem ipsum dolor sit amet, consectetur adipisicing elit, sed do eiusmod tempor incididunt ut labore et dolore magna aliqua. Ut enim ad minim veniam, quis nostrud.<br><br>consectetur adipisicing elit, sed do eiusmod tempor incididunt ut labore Lorem ipsum dolor sit amet, et dolore magna aliqua. Ut enim ad minim veniam, quis nostrud.</div>
  <div class="bottom-text lorem">Lorem ipsum dolor sit amet, consectetur adipisicing elit, sed do eiusmod tempor incididunt ut labore et dolore magna aliqua. Ut enim ad minim veniam, quis nostrud exercitation ullamco laboris nisi ut aliquip ex ea commodo consequat. Duis aute irure dolor in reprehenderit in voluptate velit esse cillum dolore eu fugiat nulla pariatur. Excepteur sint occaecat cupidatat non proident, sunt in culpa qui officia deserunt mollit anim id est laborum.</div>
</section>

<!-- Slide: pie chart -->
<section class="piece slide pie-slide row2 col2">
  <div class="heading">Heading Here</div>
  <div class="subheading">Sub Heading</div>
  <div class="rule"></div>
  <div class="left-text lorem">Lorem ipsum dolor sit amet, consectetur adipisicing elit, sed do eiusmod tempor incididunt ut labore et dolore magna aliqua. Ut enim ad minim veniam, quis nostrud exercitation ullamco laboris nisi ut aliquip ex ea commodo consequat. Duis aute irure dolor in reprehenderit in voluptate velit esse cillum dolore eu fugiat nulla pariatur. Excepteur sint occaecat cupidatat non proident, sunt in culpa qui officia deserunt mollit anim id est laborum. Ut enim ad minim veniam, quis nostrud exercitation ullamco laboris nisi ut aliquip ex ea commodo consequat.</div>
  <div class="left-text2 lorem">Excepteur sint occaecat cupidatat non proident, sunt in culpa qui officia deserunt mollit anim id est laborum. Ut enim ad minim veniam, quis nostrud exercitation ullamco laboris nisi ut aliquip ex ea commodo consequat.</div>
  <svg class="pie" width="60" height="60" viewBox="-30 -30 60 60">
    <path class="fill-gold" d="M0 0 L0 -28 A28 28 0 0 0 -5 27.5 Z" transform="translate(-1 0)"/>
    <path class="fill-ink" d="M0 0 L0 -28 A28 28 0 0 1 24 -14 Z" transform="translate(1 -1)"/>
    <path class="fill-gold" d="M0 0 L24 -14 A28 28 0 0 1 26 10 Z" transform="translate(2 0)"/>
    <path class="fill-ink" d="M0 0 L26 10 A28 28 0 0 1 -5 27.5 Z" transform="translate(1 1)"/>
  </svg>
  <div class="legend">
    <div><i style="background:var(--gold)"></i>Lorem ipsum dolor sit amet 50%</div>
    <div><i style="background:var(--ink)"></i>Duis aute irure dolor in 50%</div>
  </div>
  <div class="legend-note lorem">sunt in culpa qui officia deserunt mollit anim id est laborum. Ut enim ad minim veniam</div>
</section>

<!-- Slide: closing -->
<section class="piece slide thanks-slide row2 col3">
  <div class="thanks">Thanks</div>
  <div class="for-coming">For Coming</div>
  <div class="footer-info">
    Bramwell Court, 14 Orchard Rise, Larchmere, Ashvale, LV9 2QT<br>
    <span class="gold">P:</span> +44 0113 872 604 &nbsp;<span class="gold">M:</span> +44 7312 908 271 &nbsp;<span class="gold">E:</span> maren@veltorathletic-example.com<br>
    <span class="gold">W:</span> veltorathletic-example.com | Company number 20948367
  </div>
</section>

</body>
</html>
```